Female Leadership Word/PDF template

I need a template, not just a design, for a word document in A4 size with a cover, middle pages and last page to give a nice as course material for a leadership training. I need it as a document to directly work in myself, to put in the text etc, ready to use , not just the design. I have attached 3 files. One that is an inspiration for how I like to have it (except the photos), one that is my style guide that shows the different elements to play with. I like it to be bright and stylish at the same time. I've added another document that shows some bright colors. My web page is www.brightpathgroup.se

Target Market(s)

Women leaders who like to perform but want to increase the soft and spiritual side in their lives and profession.

Industry/Entity Type

Leadership

Font styles to use
Sans Serif

Colors

Designer to choose colors to be used in the design.

Requirements
Must have
• Feel elegant, warm, welcoming and professional.
• Must be a document I can work in, not just a design that I should apply. Willing to pay more for that.
Should not have
• Dull. Hard.

```html
<!DOCTYPE html>
<html lang="en">
<head>
<meta charset="utf-8">
<title>Bright Path – Leadership Course Template</title>
<link href="https://fonts.googleapis.com/css2?family=Domine:wght@700&family=Raleway:wght@400;500;600&display=swap" rel="stylesheet">
<style>
  :root{
    --magenta:#c8297f;
    --magenta-deep:#b81f72;
    --pink-soft:#e391bf;
    --pink-line:#e07aae;
    --orange:#e8951c;
    --navy:#2a3048;
    --grey-row:#e4e4e6;
    --paper:#ffffff;
    --canvas:#ffffff;
    --ink:#333;
  }
  *{box-sizing:border-box;margin:0;padding:0}
  html,body{width:1200px;height:1200px;overflow:hidden;background:var(--canvas)}
  body{position:relative;font-family:'Raleway',sans-serif;color:var(--ink)}
  .page{position:absolute;overflow:hidden;background:var(--paper)}
  .page.spread{top:52px;width:283px;height:400px;box-shadow:3px 4px 8px rgba(0,0,0,.35)}
  .abs{position:absolute}
  .slab{font-family:'Domine',serif;font-weight:700}
  .pink-bg{background:var(--magenta)}
  .pattern-area{position:absolute;border-radius:50%}
  .pattern-on-pink{background:radial-gradient(circle,rgba(255,255,255,.28) 0%,rgba(255,255,255,.12) 45%,rgba(255,255,255,.22) 70%,rgba(255,255,255,0) 72%)}
  .pattern-faint{background:radial-gradient(circle,rgba(200,41,127,.05) 0%,rgba(200,41,127,.03) 60%,rgba(200,41,127,0) 71%)}
  .header-band{position:absolute;left:0;top:0;width:100%;background:var(--magenta);color:#fff}
  .header-band .band-pattern{position:absolute;top:0;right:0;height:100%;background:linear-gradient(90deg,rgba(255,255,255,0),rgba(255,255,255,.28) 25%,rgba(255,255,255,.22))}
  .header-band .band-title{position:absolute;white-space:nowrap}
  .footer-rule{position:absolute;height:1px;background:var(--pink-line)}
  .toc-title{color:var(--magenta);font-size:7.5px}
  .toc-row{position:absolute;display:flex;align-items:flex-end;font-size:5px;color:#444;right:34px}
  .toc-row .dots{flex:1;border-bottom:1px dotted #555;margin:0 1px 1px}
  .toc-row.lvl1{font-weight:600;font-size:5.5px;color:#111}
  .h1{color:var(--magenta)}
  .h2{color:var(--magenta)}
  .h3{color:#c0306f}
  .h4{color:var(--orange)}
  .h5{color:var(--navy)}
  .tlabel{color:#111}
  .rule{position:absolute;height:1px;background:var(--pink-line)}
  .table-head{position:absolute;display:flex;align-items:center;color:#fff;font-weight:500}
  .table-head span{flex:1}
  .table-head.plain{color:var(--magenta);background:none}
  .grey-row{position:absolute;background:var(--grey-row);border-top:1px solid var(--pink-line)}
  .bullet{position:absolute;white-space:nowrap}
  .bullet::before{content:"";position:absolute;border-radius:50%;background:var(--magenta)}
  .photo{position:absolute;border:2px solid #fff;border-radius:8px;background:linear-gradient(160deg,#7a5a4c 0%,#5b4a45 35%,#d9d3cc 60%,#2b2e38 100%)}
  .brand-name{font-family:'Raleway',sans-serif;font-weight:400;white-space:nowrap}
  .brand-dot{position:absolute;border-radius:50%}
</style>
</head>
<body>

<!-- Spread: cover -->
<section class="page spread pink-bg" style="left:10px">
  <div class="abs" style="left:0;top:15px;width:100%;height:51px;background:#fff"></div>
  <div class="photo" role="img" aria-label="Portrait photo of the course leader" style="left:16px;top:27px;width:118px;height:160px"></div>
  <div class="brand-dot" style="left:143px;top:38px;width:16px;height:16px;background:var(--navy)"></div>
  <div class="abs brand-name" style="left:164px;top:38px;font-size:15px;color:var(--navy)">Bright Path</div>
  <div class="abs slab" style="left:157px;top:84px;font-size:24px;line-height:29px;color:#fff">Some<br>text here</div>
  <div class="pattern-area pattern-on-pink" role="img" aria-label="Decorative circular zigzag ornament" style="left:60px;top:180px;width:360px;height:360px"></div>
</section>

<!-- Spread: contents page -->
<section class="page spread" style="left:307px">
  <div class="header-band" style="height:27px">
    <div class="band-pattern" style="width:180px" role="img" aria-label="Zigzag ornament band"></div>
    <div class="band-title slab" style="left:11px;top:7px;font-size:10.5px">Some text here</div>
  </div>
  <div class="pattern-area pattern-faint" role="img" aria-label="Faint circular ornament" style="left:70px;top:185px;width:300px;height:300px"></div>
  <div class="abs slab toc-title" style="left:34px;top:47px">Contents</div>
  <div class="toc-row lvl1" style="left:34px;top:57px"><span>Heading 01</span><span class="dots"></span><span>3</span></div>
  <div class="toc-row" style="left:51px;top:66px;font-size:5.5px"><span>Heading 02</span><span class="dots"></span><span>3</span></div>
  <div class="toc-row" style="left:51px;top:75px"><span>Heading 03</span><span class="dots"></span><span>3</span></div>
  <div class="toc-row" style="left:51px;top:84px"><span>Heading 04</span><span class="dots"></span><span>3</span></div>
  <div class="toc-row" style="left:51px;top:94px"><span>Heading 05</span><span class="dots"></span><span>3</span></div>
  <div class="toc-row" style="left:51px;top:103px"><span>Table 01</span><span class="dots"></span><span>3</span></div>
  <div class="toc-row" style="left:51px;top:112px"><span>Table 02</span><span class="dots"></span><span>3</span></div>
  <div class="toc-row" style="left:51px;top:121px"><span>Bullet points</span><span class="dots"></span><span>3</span></div>
  <div class="toc-row" style="left:51px;top:131px"><span>Bullet numbers</span><span class="dots"></span><span>4</span></div>
  <div class="footer-rule" style="left:20px;top:376px;width:245px"></div>
</section>

<!-- Spread: styles page -->
<section class="page spread" style="left:602px">
  <div class="header-band" style="height:27px">
    <div class="band-pattern" style="width:180px" role="img" aria-label="Zigzag ornament band"></div>
    <div class="band-title slab" style="left:11px;top:7px;font-size:10.5px">Some text here</div>
  </div>
  <div class="pattern-area pattern-faint" role="img" aria-label="Faint circular ornament" style="left:70px;top:185px;width:300px;height:300px"></div>
  <div class="abs slab h1" style="left:34px;top:35px;font-size:9px">Heading 01</div>
  <div class="abs slab h2" style="left:34px;top:60px;font-size:7px">Heading 02</div>
  <div class="rule" style="left:34px;top:70px;width:214px"></div>
  <div class="abs slab h3" style="left:34px;top:84px;font-size:6px">Heading 03</div>
  <div class="abs slab h4" style="left:34px;top:106px;font-size:6px">Heading 04</div>
  <div class="abs slab h5" style="left:34px;top:127px;font-size:5.5px">Heading 05</div>
  <div class="abs slab tlabel" style="left:34px;top:147px;font-size:5.5px">Table 01</div>
  <div class="table-head pink-bg" style="left:34px;top:157px;width:214px;height:13px;font-size:4.8px;padding-left:3px"><span>Versão</span><span>Data</span><span>Autor</span><span>Comentários</span><span style="flex:1.3">Elaborado/modificado</span></div>
  <div class="rule" style="left:34px;top:183px;width:214px"></div>
  <div class="rule" style="left:34px;top:196px;width:214px"></div>
  <div class="abs slab tlabel" style="left:34px;top:219px;font-size:5.5px">Table 02</div>
  <div class="table-head plain" style="left:34px;top:230px;width:214px;height:12px;font-size:4.8px;padding-left:3px"><span>Versão</span><span>Data</span><span>Autor</span><span>Comentários</span><span style="flex:1.3">Elaborado/modificado</span></div>
  <div class="grey-row" style="left:34px;top:243px;width:214px;height:12px"></div>
  <div class="grey-row" style="left:34px;top:268px;width:214px;height:13px"></div>
  <div class="abs slab tlabel" style="left:34px;top:291px;font-size:5.5px">Bullet points</div>
  <div class="bullet" style="left:43px;top:302px;font-size:4.8px">Bullet level 1</div>
  <div class="bullet" style="left:51px;top:312px;font-size:4.8px">Bullet level 2</div>
  <div class="bullet" style="left:60px;top:319px;font-size:4.8px">Bullet level 3</div>
  <div class="bullet" style="left:68px;top:327px;font-size:4.8px">Bullet level 4</div>
  <div class="bullet" style="left:77px;top:334px;font-size:4.8px">Bullet level 5</div>
  <div class="footer-rule" style="left:20px;top:376px;width:245px"></div>
</section>

<!-- Spread: back cover -->
<section class="page spread pink-bg" style="left:898px">
  <div class="pattern-area pattern-on-pink" role="img" aria-label="Decorative half-circle zigzag ornament" style="left:-180px;top:30px;width:320px;height:320px"></div>
  <div class="brand-dot" style="left:108px;top:358px;width:12px;height:12px;background:#fff"></div>
  <div class="abs brand-name" style="left:124px;top:356px;font-size:10.5px;color:#fff">Bright Path</div>
  <div class="abs slab" style="left:109px;top:375px;font-size:6.5px;color:#fff">www.brightpathgroup.se</div>
</section>

<!-- Detail: cover lower part -->
<section class="page pink-bg" style="left:102px;top:635px;width:494px;height:171px">
  <div class="pattern-area pattern-on-pink" role="img" aria-label="Decorative circular zigzag ornament" style="left:110px;top:-110px;width:380px;height:380px"></div>
</section>

<!-- Detail: page footer -->
<section class="page" style="left:608px;top:635px;width:494px;height:171px;border:1px solid #e6e6e6">
  <div class="pattern-area pattern-faint" role="img" aria-label="Faint circular ornament" style="left:140px;top:-130px;width:360px;height:360px"></div>
  <div class="footer-rule" style="left:35px;top:132px;width:430px"></div>
</section>

<!-- Detail: headings page -->
<section class="page" style="left:102px;top:815px;width:494px;height:345px;border:1px solid #e6e6e6">
  <div class="header-band" style="height:47px;background:var(--pink-soft)">
    <div class="band-pattern" style="width:310px" role="img" aria-label="Zigzag ornament band"></div>
    <div class="band-title slab" style="left:20px;top:13px;font-size:17px">Some text here</div>
  </div>
  <div class="abs slab h1" style="left:60px;top:59px;font-size:16px">Heading 01</div>
  <div class="abs slab h2" style="left:60px;top:104px;font-size:12.5px">Heading 02</div>
  <div class="rule" style="left:59px;top:124px;width:377px"></div>
  <div class="abs slab h3" style="left:60px;top:146px;font-size:11px">Heading 03</div>
  <div class="abs slab h4" style="left:60px;top:184px;font-size:11px">Heading 04</div>
  <div class="abs slab h5" style="left:60px;top:222px;font-size:10px">Heading 05</div>
  <div class="abs slab tlabel" style="left:60px;top:258px;font-size:10px">Table 01</div>
  <div class="table-head pink-bg" style="left:60px;top:279px;width:376px;height:23px;font-size:9px;padding-left:4px"><span>Versão</span><span>Data</span><span>Autor</span><span>Comentários</span><span style="flex:1.35">Elaborado/modificado</span></div>
  <div class="rule" style="left:60px;top:324px;width:376px"></div>
</section>

<!-- Detail: bullets page -->
<section class="page" style="left:608px;top:815px;width:494px;height:345px;border:1px solid #e6e6e6">
  <div class="header-band" style="height:47px;background:var(--pink-soft)">
    <div class="band-pattern" style="width:310px" role="img" aria-label="Zigzag ornament band"></div>
    <div class="band-title slab" style="left:20px;top:13px;font-size:17px">Some text here</div>
  </div>
  <div class="abs slab tlabel" style="left:59px;top:111px;font-size:10px;color:var(--navy)">Bullet points</div>
  <div class="bullet big" style="left:74px;top:130px;font-size:10px">Bullet level 1</div>
  <div class="bullet big" style="left:74px;top:143px;font-size:10px">Bullet level 2</div>
  <div class="bullet big" style="left:74px;top:156px;font-size:10px">Bullet level 3</div>
  <div class="bullet big" style="left:74px;top:169px;font-size:10px">Bullet level 4</div>
  <div class="bullet big" style="left:74px;top:182px;font-size:10px">Bullet level 5</div>
</section>

<style>
  .bullet::before{left:-6px;top:2px;width:2.5px;height:2.5px}
  .bullet.big::before{left:-14px;top:5px;width:4px;height:4px}
</style>
</body>
</html>
```